Agriculture Business Card

I want to use my existing logo and use my tagline of "Don't Guess...Soil Test" on the card. Looking for a double sided card that will really get peoples attention.
Contact Info:
Marlow Field Crop Partners
Calvin Brusk
2716 K Lane
Otoe, NE 68592
402-555-0143
calvin.r.brusk@fieldmailbox.net

```html
<!DOCTYPE html>
<html lang="en">
<head>
<meta charset="utf-8">
<title>Marlow Field Crop Partners – Business Card</title>
<link rel="stylesheet" href="https://fonts.googleapis.com/css2?family=Montserrat:wght@400;500;700;800&display=swap">
<style>
  :root {
    --backdrop: #cfcecb;
    --card: #19191b;
    --edge: #f4b51f;
    --leaf: #39b54a;
    --copper: #a86a4c;
    --ink: #f2f2f2;
  }
  * { box-sizing: border-box; margin: 0; padding: 0; }
  html, body {
    width: 1200px; height: 801px; overflow: hidden;
    background: var(--backdrop);
    font-family: "Montserrat", Arial, sans-serif;
  }
  .sheet {
    position: relative; width: 1200px; height: 801px;
    display: flex; align-items: center; justify-content: center; gap: 50px;
  }
  .card {
    position: relative; width: 540px; height: 309px;
    background: var(--card);
    border-bottom: 5px solid var(--edge);
    border-left: 3px solid var(--edge);
    box-shadow: 0 14px 28px rgba(0,0,0,.28);
  }
  /* front */
  .front .brand {
    position: absolute; top: 40px; right: 44px; width: 230px;
    display: flex; align-items: center; gap: 10px;
  }
  .brand-dot { width: 16px; height: 16px; border-radius: 50%; background: var(--edge); flex: none; }
  .front .brand-name {
    color: var(--copper); font-weight: 700; font-size: 16px; line-height: 1.15;
  }
  .contact {
    position: absolute; top: 126px; right: 44px; width: 230px;
    color: var(--ink); font-size: 12.5px; line-height: 1.5; list-style: none;
  }
  .contact li { display: flex; align-items: center; gap: 6px; white-space: nowrap; }
  .contact .address { margin-bottom: 10px; display: block; }
  .contact svg { width: 11px; height: 11px; flex: none; fill: var(--leaf); }
  .holder {
    position: absolute; left: 40px; bottom: 44px;
    color: var(--leaf); font-weight: 800; font-size: 27px; letter-spacing: .5px;
  }
  /* back */
  .back {
    display: flex; flex-direction: column; align-items: center; justify-content: center; gap: 22px;
  }
  .back .brand { display: flex; align-items: center; gap: 14px; }
  .back .brand-dot { width: 34px; height: 34px; }
  .back .brand-name { font-weight: 700; font-size: 28px; line-height: 1.15; width: 270px; color: var(--edge); }
  .tagline {
    color: var(--leaf); font-weight: 700; font-size: 16px; letter-spacing: 1.5px; text-transform: uppercase;
  }
</style>
</head>
<body>
<main class="sheet">
  <section class="card front" aria-label="Card front">
    <div class="brand">
      <span class="brand-dot"></span>
      <span class="brand-name">Marlow Field Crop Partners</span>
    </div>
    <ul class="contact">
      <li class="address">2716 K Lane<br>Otoe, NE 68592</li>
      <li>
        <svg viewBox="0 0 24 24" aria-hidden="true"><path d="M6.6 10.8a15 15 0 0 0 6.6 6.6l2.2-2.2a1 1 0 0 1 1-.25 11.4 11.4 0 0 0 3.6.57 1 1 0 0 1 1 1V20a1 1 0 0 1-1 1A17 17 0 0 1 3 4a1 1 0 0 1 1-1h3.5a1 1 0 0 1 1 1c0 1.25.2 2.45.57 3.6a1 1 0 0 1-.25 1z"/></svg>
        402-555-0143
      </li>
      <li>
        <svg viewBox="0 0 24 24" aria-hidden="true"><path d="M2 5h20v14H2z M2 5l10 8 10-8" stroke="#19191b" stroke-width="1.5"/></svg>
        calvin.r.brusk@fieldmailbox.net
      </li>
    </ul>
    <h1 class="holder">CALVIN BRUSK</h1>
  </section>

  <section class="card back" aria-label="Card back">
    <div class="brand">
      <span class="brand-dot"></span>
      <span class="brand-name">Marlow Field Crop Partners</span>
    </div>
    <p class="tagline">Don't Guess...Soil Test</p>
  </section>
</main>
</body>
</html>
```